Redesign of PTO Calendar website

Looking to drastically improve our PTO (paid time off) Calendar look and feel. Need a modern and well thought out design that is fun.
Current Screenshots
https://files.brindlemoor.net/sheet/p/7vTq2LmW9xZpK4nRb8JsYcHa3eDfG5uNwQ1tVhXo/view?mode=public
It's written in PHP and Laravel, if that matters. I am not necessarily attached to any of the current design, so please go wild. Current functionality needs to remain the same, but some can be added if you feel it would be of value. Layout can certainly change.
NOTE - this calendar can be used by any company, not just our own. So we'd like it to have a look and feel that is easy to navigate.
Site logo is attached.
Pages needed:
* Login Page
* Registration Page
* Calendar page
* Add PTO method
* Admin page (will use template for all admin areas)
* User profile page
Thanks!

```html
<!DOCTYPE html>
<html lang="en">
<head>
<meta charset="utf-8">
<title>Restday – PTO Calendar</title>
<link rel="stylesheet" href="https://fonts.googleapis.com/css2?family=Roboto:wght@400;500;700&family=Lato:wght@400;700&display=swap">
<style>
:root{
  --page:#f4f5f7;
  --navy:#3c4b62;
  --navy-dark:#34425a;
  --blue:#1a73bd;
  --blue-bright:#1e82d2;
  --blue-btn:#1f5f98;
  --ink:#2b2f36;
  --muted:#6b7280;
  --line:#d9dde3;
  --white:#ffffff;
  --tag:#8fb9e6;
  --chat-hi:#e8f0fb;
}
*{box-sizing:border-box;margin:0;padding:0}
html,body{width:1200px;height:2264px;overflow:hidden}
body{background:var(--page);font-family:"Roboto",sans-serif;color:var(--ink);position:relative}

/* ---------- login ---------- */
.login{position:absolute;left:48px;top:50px;width:1104px;height:679px;overflow:hidden;box-shadow:0 2px 6px rgba(0,0,0,.15)}
.login-bg{position:absolute;inset:0;background:linear-gradient(135deg,#2f5f93 0%,#3f78ad 45%,#4a86bf 100%)}
.login-title{position:absolute;top:108px;width:100%;text-align:center;color:var(--white);font-size:40px;font-weight:500;letter-spacing:.2px}
.login-sub{position:absolute;top:164px;width:100%;text-align:center;color:var(--white);font-family:"Lato",sans-serif;font-size:18px}
.login-sub b{font-weight:700}
.login-card{position:absolute;left:340px;top:218px;width:424px;height:343px;background:var(--white);border-radius:10px}
.brand{display:flex;align-items:center;justify-content:center;gap:8px;font-family:"Roboto",sans-serif;font-weight:700;color:var(--navy);white-space:nowrap}
.login-card .brand{position:absolute;top:30px;width:100%;font-size:30px}
.brand .dot{width:22px;height:22px;border-radius:50%;background:var(--blue)}
.field-label{position:absolute;left:59px;font-size:14px;font-weight:500;color:var(--ink)}
.field{position:absolute;left:59px;width:306px;height:37px;border:1px solid #cfd4da;background:var(--white);font-family:"Lato",sans-serif;font-size:12px;display:flex;align-items:center;padding-left:12px}
.dots{display:flex;gap:4px}
.dots i{width:10px;height:10px;border-radius:50%;background:#222}
.signin{position:absolute;left:139px;top:244px;width:147px;height:40px;border-radius:4px;background:linear-gradient(#2a6aa7,#1d4f80);color:var(--white);font-family:"Lato",sans-serif;font-weight:700;font-size:15px;display:flex;align-items:center;justify-content:center;box-shadow:0 3px 6px rgba(0,0,0,.25)}
.forgot{position:absolute;top:297px;width:100%;text-align:center;font-family:"Lato",sans-serif;font-size:12px;color:var(--blue)}

/* ---------- dashboard ---------- */
.app{position:absolute;left:48px;width:1104px;height:679px;background:var(--white);overflow:hidden;box-shadow:0 2px 6px rgba(0,0,0,.15)}
.app.one{top:784px}
.app.two{top:1518px}
.sidebar{position:absolute;left:0;top:0;width:158px;height:100%;background:var(--navy)}
.sidebar .brand{position:absolute;top:26px;left:0;width:158px;color:var(--white);font-size:27px;gap:6px}
.sidebar .brand .dot{background:var(--white);width:20px;height:20px}
.nav-head{position:absolute;left:20px;top:98px;color:var(--white);font-size:14px;font-weight:500;letter-spacing:.3px}
.nav-item{position:absolute;left:0;width:158px;height:48px;display:flex;align-items:center;gap:10px;padding-left:20px;color:var(--white);font-size:14px}
.nav-item svg{width:22px;height:22px;stroke:currentColor;fill:none;stroke-width:1.4}
.nav-item.active{background:var(--white);color:var(--blue)}
.page-title{position:absolute;left:179px;top:22px;font-size:19px;font-weight:700;color:var(--blue);letter-spacing:.3px}
.search{position:absolute;left:652px;top:13px;width:276px;height:39px;border:1px solid #eceef1;font-size:11px;color:#444;display:flex;align-items:center;padding-left:11px}
.search-btn{position:absolute;left:928px;top:13px;width:40px;height:39px;background:var(--blue-bright);display:flex;align-items:center;justify-content:center}
.bell{position:absolute;left:993px;top:20px}
.bell .badge{position:absolute;right:-3px;top:-2px;width:8px;height:8px;border-radius:50%;background:var(--blue-bright)}
.avatar-me{position:absolute;left:1022px;top:12px;width:34px;height:34px;border-radius:50%;background:#3a3f44}
.caret{position:absolute;left:1066px;top:26px;border:5px solid transparent;border-top:6px solid var(--blue-bright)}

.calendar{position:absolute;left:177px;top:74px;width:704px;box-shadow:0 1px 4px rgba(0,0,0,.12)}
.cal-head{height:44px;background:var(--navy);color:var(--white);display:flex;align-items:center;justify-content:center;gap:22px;font-size:21px;font-weight:700;letter-spacing:.5px}
.cal-head svg{stroke:var(--white);fill:none;stroke-width:1.6}
.cal-grid{display:grid;grid-template-columns:97px 96px 96px 120px 104px 84px 107px}
.cal-grid.days{background:var(--blue-bright);color:var(--white);font-size:14px;font-weight:500}
.cal-grid.days div{height:35px;display:flex;align-items:center;justify-content:center;border-right:1px solid rgba(255,255,255,.25)}
.cal-grid.dates{grid-template-rows:49px 60px 60px 60px 54px}
.cal-grid.dates div{border-right:1px solid var(--line);border-bottom:1px solid var(--line);display:flex;flex-direction:column;align-items:center;justify-content:center;font-size:14px;font-weight:500}
.cal-grid.dates .pto{background:var(--blue-bright);color:var(--white);font-size:9.5px;line-height:1.1;text-align:center}
.cal-grid.dates .pto b{font-size:13px;margin-bottom:3px}

.chat{position:absolute;left:891px;top:74px;width:201px;height:361px;background:var(--white);box-shadow:0 1px 4px rgba(0,0,0,.12);font-size:7px;overflow:hidden}
.chat-top{height:26px;display:flex;align-items:center;justify-content:space-between;padding:0 12px 0 14px;color:#37a05a;font-size:6px}
.chat-top .mini{width:14px;height:14px;border-radius:50%;background:#a9b7c9}
.chat-tabs{display:flex;height:26px;font-size:7px}
.chat-tabs div{flex:1;display:flex;align-items:center;justify-content:center}
.chat-tabs .on{border-top:2px solid var(--blue-bright)}
.chat-tabs .off{background:#eef1f5;color:#666}
.pill{margin:8px auto 10px;width:110px;height:14px;border-radius:7px;background:#eef1f5;display:flex;font-size:6.5px}
.pill span{flex:1;display:flex;align-items:center;justify-content:center}
.pill .on{background:var(--white);border-radius:7px;margin:1px}
.msg{display:flex;gap:6px;padding:3px 6px 5px 14px;line-height:1.35}
.msg.hi{background:var(--chat-hi);margin:0 4px;padding-left:10px}
.msg i{flex:none;width:10px;height:10px;border-radius:50%;background:#7c8ea8;margin-top:2px}
.msg b{font-weight:700}
.msg em{font-style:normal;color:#9aa3ad;font-size:5.5px}
.msg .org{color:var(--blue-bright)}

.events{position:absolute;left:177px;top:454px;width:915px;height:204px;box-shadow:0 1px 4px rgba(0,0,0,.12);display:grid;grid-template-columns:repeat(4,1fr)}
.event{position:relative;padding:17px 0 0 21px}
.tag{display:inline-block;background:var(--tag);color:var(--white);font-size:11px;padding:2px 10px;border-radius:3px}
.event h3{margin-top:10px;font-size:16px;font-weight:500;line-height:1.22;letter-spacing:.2px}
.event p{margin-top:10px;font-size:11px;line-height:1.65}
.event .time{margin-top:6px;font-size:11px}
.people{display:flex;margin-top:10px}
.people span{width:27px;height:27px;border-radius:50%;background:linear-gradient(#5d4a43,#c79c86);border:2px solid var(--white);margin-right:-3px}

.dim{position:absolute;inset:0;background:rgba(70,72,78,.55)}
.modal{position:absolute;left:360px;top:101px;width:385px;height:476px;background:var(--white);border-radius:8px;overflow:hidden;box-shadow:0 4px 18px rgba(0,0,0,.3)}
.modal-head{height:57px;background:var(--blue);color:var(--white);display:flex;align-items:center;justify-content:space-between;padding:0 16px 0 37px;font-size:15px;font-weight:500}
.modal .field-label{left:40px;font-size:14px}
.modal .field{left:40px;justify-content:space-between;padding-right:12px}
.arrow-down{border:5px solid transparent;border-top:7px solid #555;margin-top:6px}
.btn{position:absolute;top:406px;width:95px;height:40px;border-radius:3px;color:var(--white);font-size:15px;font-weight:700;display:flex;align-items:center;justify-content:center;box-shadow:0 3px 6px rgba(0,0,0,.25)}
.btn.save{left:93px;background:var(--blue-btn)}
.btn.close{left:196px;background:var(--navy-dark)}
</style>
</head>
<body>

<section class="login">
  <div class="login-bg" role="img" aria-label="Blue-tinted photo of a laptop keyboard and a paper calendar with pins"></div>
  <h1 class="login-title">Let’s get started now!</h1>
  <p class="login-sub">or <b>create an account</b> if not registered yet</p>
  <div class="login-card">
    <div class="brand"><span>Restday</span><span class="dot"></span></div>
    <label class="field-label" style="top:88px">Email:</label>
    <div class="field" style="top:113px">mail@mail.com</div>
    <label class="field-label" style="top:163px">Password:</label>
    <div class="field" style="top:188px"><span class="dots"><i></i><i></i><i></i><i></i><i></i><i></i><i></i><i></i></span></div>
    <div class="signin">Sign In</div>
    <p class="forgot">Forgot pasword?</p>
  </div>
</section>

<section class="app one">
  <aside class="sidebar">
    <div class="brand"><span>Restday</span><span class="dot"></span></div>
    <div class="nav-head">GENERAL</div>
    <div class="nav-item" style="top:132px"><svg viewBox="0 0 24 24"><circle cx="6" cy="8" r="2.5"/><circle cx="12" cy="6" r="2.5"/><circle cx="18" cy="8" r="2.5"/><path d="M2 18v-4h8v4M8 16v-4h8v4M14 18v-4h8v4"/></svg>Teams</div>
    <div class="nav-item" style="top:181px"><svg viewBox="0 0 24 24"><circle cx="12" cy="8" r="4.5"/><path d="M3 22c0-5 4-8 9-8s9 3 9 8"/></svg>Members</div>
    <div class="nav-item" style="top:233px"><svg viewBox="0 0 24 24"><rect x="3" y="3" width="18" height="14"/><path d="M6 7h4M6 10h4M13 7h5M13 10h5M6 13h12M5 20h14"/></svg>PTO Types</div>
    <div class="nav-item active" style="top:294px"><svg viewBox="0 0 24 24"><rect x="3" y="5" width="18" height="16" rx="1"/><path d="M3 9h18M7 3v4M17 3v4"/><path d="M7 13h1M11 13h1M15 13h1M7 17h1M11 17h1M15 17h1"/></svg>Add PTO</div>
  </aside>
  <h2 class="page-title">ADD PTO</h2>
  <div class="search">Search Event</div>
  <div class="search-btn"><svg width="22" height="22" viewBox="0 0 24 24" fill="none" stroke="#fff" stroke-width="1.6"><circle cx="10" cy="10" r="7"/><path d="M15 15l6 6"/></svg></div>
  <div class="bell"><svg width="20" height="22" viewBox="0 0 24 24" fill="none" stroke="#444" stroke-width="1.4"><path d="M6 17V11a6 6 0 0112 0v6l2 2H4z"/><path d="M10 21h4"/></svg><span class="badge"></span></div>
  <div class="avatar-me" role="img" aria-label="User profile photo"></div>
  <span class="caret"></span>

  <div class="calendar">
    <div class="cal-head"><svg width="12" height="20" viewBox="0 0 12 20"><path d="M10 2L2 10l8 8"/></svg>AUGUST 2020<svg width="12" height="20" viewBox="0 0 12 20"><path d="M2 2l8 8-8 8"/></svg></div>
    <div class="cal-grid days"><div>Sunday</div><div>Monday</div><div>Tuesday</div><div>Wednesday</div><div>Thursday</div><div>Friday</div><div>Saturday</div></div>
    <div class="cal-grid dates">
      <div>1</div><div>2</div><div>4</div><div>5</div><div>6</div><div>7</div><div>8</div>
      <div>9</div><div>10</div><div class="pto"><b>11</b>12a Dana<br>Merrick -Va</div><div>12</div><div>13</div><div>14</div><div>15</div>
      <div>16</div><div>17</div><div>18</div><div>19</div><div>20</div><div>21</div><div>22</div>
      <div>23</div><div>24</div><div>25</div><div>26</div><div>27</div><div>28</div><div>29</div>
      <div>30</div><div>31</div><div></div><div></div><div></div><div></div><div></div>
    </div>
  </div>

  <div class="chat">
    <div class="chat-top"><span>● 2403</span><span class="mini"></span></div>
    <div class="chat-tabs"><div class="on">Chat •</div><div class="off">People</div></div>
    <div class="pill"><span class="on">Session</span><span>Event</span></div>
    <div class="msg hi"><i></i><div><b>Miko</b> · <span class="org">Organizer</span> <em>12:45</em><br>Everyone, session started!</div></div>
    <div class="msg"><i></i><div><b>Joseph</b> <em>12:30</em><br>Happy to be here, it is high-quality stuff!</div></div>
    <div class="msg"><i></i><div><b>Sara</b> <em>12:31</em><br>Arlo, can you please tell us more about the challenges during the engine launch?</div></div>
    <div class="msg"><i></i><div><b>Ronnie</b> <em>12:33</em><br>This is an amazing speech!</div></div>
    <div class="msg"><i></i><div><b>Sofia</b> <em>12:44</em><br>Which sources would you recommend to learn more about this technology?</div></div>
    <div class="msg"><i></i><div><b>Joseph</b> <em>12:47</em><br>Wow, this is such a useful lecture! Thanks, bro!</div></div>
    <div class="msg"><i></i><div><b>Ben</b> <em>12:50</em><br>I fully agree with you, Arlo!</div></div>
    <div class="msg"><i></i><div><b>Yesica</b> <em>12:51</em><br>Hi Arlo! Thanks for sharing this!</div></div>
    <div class="msg"><i></i><div><b>Sara</b> <em>12:30</em><br>What is your favorite part of the workday and</div></div>
  </div>

  <div class="events">
    <div class="event"><span class="tag">Now</span><h3>Lorem ipsum dolor amet, consectetur adipiscing</h3><p>Lorem ipsum dolor sit tetur adiscing<br>elit, sed do eiusmod r incididunt</p><div class="time">Today 9:15 - 10:30 Am</div><div class="people" role="img" aria-label="Attendee photos"><span></span><span></span><span></span></div></div>
    <div class="event"><span class="tag">Today</span><h3>Lorem ipsum dolor amet, consectetur adipiscing</h3><p>Lorem ipsum dolor sit tetur adiscing<br>elit, sed do eiusmod r incididunt</p><div class="time">Today 11:15 - 1:30 Pm</div><div class="people" role="img" aria-label="Attendee photos"><span></span><span></span><span></span></div></div>
    <div class="event"><span class="tag">Now</span><h3>Lorem ipsum dolor amet, consectetur adipiscing</h3><p>Lorem ipsum dolor sit tetur adiscing<br>elit, sed do eiusmod r incididunt</p><div class="time">Today 8:30 - 10:30 Am</div><div class="people" role="img" aria-label="Attendee photos"><span></span><span></span><span></span></div></div>
    <div class="event"><span class="tag">Now</span><h3>Lorem ipsum dolor amet, consectetur adipiscing</h3><p>Lorem ipsum dolor sit tetur adiscing<br>elit, sed do eiusmod r incididunt</p><div class="time">Today 9:15 - 10:30 Am</div><div class="people" role="img" aria-label="Attendee photos"><span></span><span></span><span></span></div></div>
  </div>
</section>

<section class="app two">
  <aside class="sidebar">
    <div class="brand"><span>Restday</span><span class="dot"></span></div>
    <div class="nav-head">GENERAL</div>
    <div class="nav-item" style="top:132px"><svg viewBox="0 0 24 24"><circle cx="6" cy="8" r="2.5"/><circle cx="12" cy="6" r="2.5"/><circle cx="18" cy="8" r="2.5"/><path d="M2 18v-4h8v4M8 16v-4h8v4M14 18v-4h8v4"/></svg>Teams</div>
    <div class="nav-item" style="top:181px"><svg viewBox="0 0 24 24"><circle cx="12" cy="8" r="4.5"/><path d="M3 22c0-5 4-8 9-8s9 3 9 8"/></svg>Members</div>
    <div class="nav-item" style="top:233px"><svg viewBox="0 0 24 24"><rect x="3" y="3" width="18" height="14"/><path d="M6 7h4M6 10h4M13 7h5M13 10h5M6 13h12M5 20h14"/></svg>PTO Types</div>
    <div class="nav-item active" style="top:294px"><svg viewBox="0 0 24 24"><rect x="3" y="5" width="18" height="16" rx="1"/><path d="M3 9h18M7 3v4M17 3v4"/><path d="M7 13h1M11 13h1M15 13h1M7 17h1M11 17h1M15 17h1"/></svg>Add PTO</div>
  </aside>
  <h2 class="page-title">ADD PTO</h2>
  <div class="search">Search Event</div>
  <div class="search-btn"><svg width="22" height="22" viewBox="0 0 24 24" fill="none" stroke="#fff" stroke-width="1.6"><circle cx="10" cy="10" r="7"/><path d="M15 15l6 6"/></svg></div>
  <div class="bell"><svg width="20" height="22" viewBox="0 0 24 24" fill="none" stroke="#444" stroke-width="1.4"><path d="M6 17V11a6 6 0 0112 0v6l2 2H4z"/><path d="M10 21h4"/></svg><span class="badge"></span></div>
  <div class="avatar-me" role="img" aria-label="User profile photo"></div>
  <span class="caret"></span>

  <div class="calendar">
    <div class="cal-head"><svg width="12" height="20" viewBox="0 0 12 20"><path d="M10 2L2 10l8 8"/></svg>AUGUST 2020<svg width="12" height="20" viewBox="0 0 12 20"><path d="M2 2l8 8-8 8"/></svg></div>
    <div class="cal-grid days"><div>Sunday</div><div>Monday</div><div>Tuesday</div><div>Wednesday</div><div>Thursday</div><div>Friday</div><div>Saturday</div></div>
    <div class="cal-grid dates">
      <div>1</div><div>2</div><div>4</div><div>5</div><div>6</div><div>7</div><div>8</div>
      <div>9</div><div>10</div><div class="pto"><b>11</b>12a Dana<br>Merrick -Va</div><div>12</div><div>13</div><div>14</div><div>15</div>
      <div>16</div><div>17</div><div>18</div><div>19</div><div>20</div><div>21</div><div>22</div>
      <div>23</div><div>24</div><div>25</div><div>26</div><div>27</div><div>28</div><div>29</div>
      <div>30</div><div>31</div><div></div><div></div><div></div><div></div><div></div>
    </div>
  </div>

  <div class="chat">
    <div class="chat-top"><span>● 2403</span><span class="mini"></span></div>
    <div class="chat-tabs"><div class="on">Chat •</div><div class="off">People</div></div>
    <div class="pill"><span class="on">Session</span><span>Event</span></div>
    <div class="msg hi"><i></i><div><b>Miko</b> · <span class="org">Organizer</span> <em>12:45</em><br>Everyone, session started!</div></div>
    <div class="msg"><i></i><div><b>Joseph</b> <em>12:30</em><br>Happy to be here, it is high-quality stuff!</div></div>
    <div class="msg"><i></i><div><b>Sara</b> <em>12:31</em><br>Arlo, can you please tell us more about the challenges during the engine launch?</div></div>
    <div class="msg"><i></i><div><b>Ronnie</b> <em>12:33</em><br>This is an amazing speech!</div></div>
    <div class="msg"><i></i><div><b>Sofia</b> <em>12:44</em><br>Which sources would you recommend to learn more about this technology?</div></div>
    <div class="msg"><i></i><div><b>Joseph</b> <em>12:47</em><br>Wow, this is such a useful lecture! Thanks, bro!</div></div>
    <div class="msg"><i></i><div><b>Ben</b> <em>12:50</em><br>I fully agree with you, Arlo!</div></div>
    <div class="msg"><i></i><div><b>Yesica</b> <em>12:51</em><br>Hi Arlo! Thanks for sharing this!</div></div>
    <div class="msg"><i></i><div><b>Sara</b> <em>12:30</em><br>What is your favorite part of the workday and</div></div>
  </div>

  <div class="events">
    <div class="event"><span class="tag">Now</span><h3>Lorem ipsum dolor amet, consectetur adipiscing</h3><p>Lorem ipsum dolor sit tetur adiscing<br>elit, sed do eiusmod r incididunt</p><div class="time">Today 9:15 - 10:30 Am</div><div class="people" role="img" aria-label="Attendee photos"><span></span><span></span><span></span></div></div>
    <div class="event"><span class="tag">Today</span><h3>Lorem ipsum dolor amet, consectetur adipiscing</h3><p>Lorem ipsum dolor sit tetur adiscing<br>elit, sed do eiusmod r incididunt</p><div class="time">Today 11:15 - 1:30 Pm</div><div class="people" role="img" aria-label="Attendee photos"><span></span><span></span><span></span></div></div>
    <div class="event"><span class="tag">Now</span><h3>Lorem ipsum dolor amet, consectetur adipiscing</h3><p>Lorem ipsum dolor sit tetur adiscing<br>elit, sed do eiusmod r incididunt</p><div class="time">Today 8:30 - 10:30 Am</div><div class="people" role="img" aria-label="Attendee photos"><span></span><span></span><span></span></div></div>
    <div class="event"><span class="tag">Now</span><h3>Lorem ipsum dolor amet, consectetur adipiscing</h3><p>Lorem ipsum dolor sit tetur adiscing<br>elit, sed do eiusmod r incididunt</p><div class="time">Today 9:15 - 10:30 Am</div><div class="people" role="img" aria-label="Attendee photos"><span></span><span></span><span></span></div></div>
  </div>

  <div class="dim"></div>
  <div class="modal">
    <div class="modal-head"><span>Add PTO</span><svg width="12" height="12" viewBox="0 0 12 12" stroke="#fff" stroke-width="1.5"><path d="M1 1l10 10M11 1L1 11"/></svg></div>
    <label class="field-label" style="top:94px">Member</label>
    <div class="field" style="top:110px">Dana Merrick<span class="arrow-down"></span></div>
    <label class="field-label" style="top:172px">PTO Type</label>
    <div class="field" style="top:188px">Vacation<span class="arrow-down"></span></div>
    <label class="field-label" style="top:251px">Start Date</label>
    <div class="field" style="top:266px">08/11/2020<svg width="16" height="16" viewBox="0 0 24 24" fill="none" stroke="#555" stroke-width="1.4"><rect x="3" y="5" width="18" height="16"/><path d="M3 9h18M7 3v4M17 3v4M7 13h1M11 13h1M15 13h1M7 17h1M11 17h1M15 17h1"/></svg></div>
    <label class="field-label" style="top:329px">End Date</label>
    <div class="field" style="top:344px">08/14/2020<svg width="16" height="16" viewBox="0 0 24 24" fill="none" stroke="#555" stroke-width="1.4"><rect x="3" y="5" width="18" height="16"/><path d="M3 9h18M7 3v4M17 3v4M7 13h1M11 13h1M15 13h1M7 17h1M11 17h1M15 17h1"/></svg></div>
    <div class="btn save">Save</div>
    <div class="btn close">Close</div>
  </div>
</section>

</body>
</html>
```